business card, stationary, email signature, envelopes
Bold Grins, PLLC
business card, stationary, email signature, envelopes - Medical
Creative Brief
Bright & Fun-filled
714 Harwick Ave Dover, NH 03827
boldgrinspllc@quorvamail.com
BoldGrinsPLLC.com

```html
<!DOCTYPE html>
<html lang="en">
<head>
<meta charset="utf-8">
<title>Bold Grins, PLLC – Business Card</title>
<link href="https://fonts.googleapis.com/css2?family=Montserrat:wght@400;500&display=swap" rel="stylesheet">
<style>
  :root {
    --canvas: #d9dade;
    --card: #ffffff;
    --navy: #33507f;
    --pink: #e1336e;
    --brand-blue: #2f64a8;
    --name-blue: #2c8fc9;
    --ink: #3b3f47;
    --white: #ffffff;
  }
  * { margin: 0; padding: 0; box-sizing: border-box; }
  html, body { width: 1200px; height: 670px; overflow: hidden; }
  body {
    background: var(--canvas);
    font-family: "Montserrat", Arial, sans-serif;
    position: relative;
  }
  .card {
    position: absolute;
    top: 185px;
    width: 540px;
    height: 300px;
    background: var(--card);
    box-shadow: 0 10px 24px rgba(0,0,0,.18);
    overflow: hidden;
  }
  .card-front { left: 45px; }
  .card-back { left: 615px; }

  .brand-name {
    font-family: "Montserrat", Arial, sans-serif;
    font-weight: 500;
    color: var(--brand-blue);
    white-space: nowrap;
  }
  .card-front .brand-name {
    position: absolute;
    left: 50%; top: 50%;
    transform: translate(-50%, -50%);
    font-size: 32px;
  }

  .card-back .wave { position: absolute; inset: 0; }
  .card-back .brand-name {
    position: absolute;
    left: 30px; top: 40px;
    font-size: 22px;
  }

  .holder {
    position: absolute;
    left: 40px; top: 176px;
  }
  .holder-name {
    font-size: 13px;
    font-weight: 500;
    letter-spacing: 1px;
    color: var(--name-blue);
  }
  .holder-role {
    font-size: 10px;
    color: var(--ink);
    margin-top: 3px;
  }

  .contact {
    position: absolute;
    right: 22px; top: 76px;
    list-style: none;
    color: var(--white);
    font-size: 8.5px;
    line-height: 1.35;
  }
  .contact li {
    display: flex;
    align-items: center;
    justify-content: flex-end;
    gap: 6px;
    margin-bottom: 7px;
  }
  .contact .address { margin-bottom: 12px; text-align: right; display: block; }
  .contact svg { width: 9px; height: 9px; flex: none; }
</style>
</head>
<body>

  <section class="card card-front" aria-label="Business card front">
    <p class="brand-name">Bold Grins, PLLC</p>
  </section>

  <section class="card card-back" aria-label="Business card back">
    <svg class="wave" viewBox="0 0 540 300" preserveAspectRatio="none" aria-hidden="true">
      <path fill="var(--pink)" d="M0,244 C160,244 250,215 320,138 C380,70 450,30 540,20 L540,300 L0,300 Z"/>
      <path fill="var(--navy)" d="M0,260 C170,260 268,230 336,156 C396,90 462,54 540,46 L540,300 L0,300 Z"/>
    </svg>

    <p class="brand-name">Bold Grins, PLLC</p>

    <div class="holder">
      <p class="holder-name">MARCUS ELLERY</p>
      <p class="holder-role">Managing Director</p>
    </div>

    <ul class="contact">
      <li class="address">714 Harwick Ave<br>Dover, NH 03827</li>
      <li>Tel 603 555 0148
        <svg viewBox="0 0 10 10"><path fill="var(--white)" d="M2 1l2 2-1 1.2c.6 1.2 1.5 2.1 2.8 2.8L7 6l2 2-1.4 1.4C4.6 9 1 5.4.6 2.4z"/></svg></li>
      <li>Fax 603 555 0149
        <svg viewBox="0 0 10 10"><rect x="1" y="3" width="8" height="5" fill="var(--white)"/><rect x="3" y="1" width="4" height="2" fill="var(--white)"/></svg></li>
      <li>Cell 603 555 0150
        <svg viewBox="0 0 10 10"><rect x="2.5" y="0.5" width="5" height="9" rx="1" fill="var(--white)"/></svg></li>
      <li>boldgrinspllc@quorvamail.com
        <svg viewBox="0 0 10 10"><rect x="0.5" y="2" width="9" height="6" fill="var(--white)"/><path d="M0.5 2l4.5 3.5L9.5 2" fill="none" stroke="var(--navy)" stroke-width="0.8"/></svg></li>
      <li>BoldGrinsPLLC.com
        <svg viewBox="0 0 10 10"><circle cx="5" cy="5" r="4.2" fill="none" stroke="var(--white)"/><path d="M1 5h8M5 .8c2 2.5 2 5.9 0 8.4M5 .8c-2 2.5-2 5.9 0 8.4" fill="none" stroke="var(--white)" stroke-width="0.7"/></svg></li>
    </ul>
  </section>

</body>
</html>
```